Brindle's Homes website

We need a simple website for our property investment business in the UK. We basically need our contact details and brief description.We have the company logo already done (via ArtPlinth) so please use these:https://drive.google.com/drive/folders/1szJ3iRhelElZ40NIFT7w-c14MaY3Y_oV?usp=sharingYou could use some stock photos of UK houses for now.Let me know when to provide more detailed descriptions, etc

Coding

Coded - Design and coding required

Number of Pages Required

1 page

Colors

Designer to choose colors to be used in the design.

```html
<!DOCTYPE html>
<html lang="en">
<head>
<meta charset="utf-8">
<title>Brindle's Homes</title>
<link rel="stylesheet" href="https://fonts.googleapis.com/css2?family=Questrial&family=Poppins:wght@500;600;700&display=swap">
<style>
:root{
  --ink:#111111;
  --text:#333333;
  --muted:#555555;
  --line:#d8d8d8;
  --band:#f4f4f4;
  --white:#ffffff;
  --footer:#2b2b2b;
  --footer-text:#c9c9c9;
  --star:#f2a31b;
  --pin:#e0282e;
}
*{box-sizing:border-box;margin:0;padding:0}
html,body{width:1200px;height:2594px;overflow:hidden}
body{position:relative;background:var(--white);font-family:"Questrial",sans-serif;color:var(--text)}
.abs{position:absolute}
.heading{font-family:"Poppins",sans-serif;font-weight:600;color:var(--ink)}
.btn-dark{background:var(--ink);color:var(--white);display:flex;align-items:center;justify-content:center}

/* header */
.brand{display:flex;align-items:center;gap:7px;font-size:14px;letter-spacing:3px;color:var(--ink)}
.brand-square{width:12px;height:12px;background:var(--ink)}
.topline{right:240px;top:20px;font-size:9px;color:var(--muted)}
.topline b{color:var(--ink);font-family:"Poppins",sans-serif;font-weight:600}
.nav{top:52px;left:500px;display:flex;gap:0;font-size:11px;color:var(--ink)}
.nav span{margin-right:20px}
.btn-outline{border:1px solid var(--ink);font-size:11px;color:var(--ink);display:flex;align-items:center;justify-content:center}

/* hero */
.hero{left:0;top:92px;width:1200px;height:343px;background:linear-gradient(180deg,#3a62a8 0%,#7795c6 28%,#6b4a31 55%,#4a2f1e 80%,#8a7458 100%)}
.hero-title{top:208px;width:1200px;text-align:center;color:var(--white);font-family:"Poppins",sans-serif;font-weight:700;font-size:19px}
.hero-sub{top:238px;width:1200px;text-align:center;color:var(--white);font-size:12px}
.search{left:297px;top:265px;width:600px;height:55px;background:rgba(255,255,255,.35)}
.field{background:var(--white);font-size:9px;color:var(--muted);display:flex;align-items:center;padding-left:10px}

/* what we do */
.wwd-title{left:234px;top:497px;font-size:25px;font-weight:700}
.wwd-sub{left:234px;top:530px;font-size:13px;font-family:"Poppins",sans-serif;font-weight:500;color:var(--ink)}
.wwd-text{left:234px;top:555px;width:330px;font-size:9.3px;line-height:15px;text-align:justify;color:var(--muted)}
.photo{background:linear-gradient(180deg,#5b8fd0 0%,#a8c4e0 30%,#e7dcc2 55%,#587a3c 85%,#3e5b2a 100%)}
.frame{border-left:1px solid var(--ink);border-bottom:1px solid var(--ink);border-right:1px solid var(--ink)}

/* find property */
.center{width:1200px;text-align:center}
.section-title{font-size:19px}
.section-sub{font-size:10px;color:var(--muted)}
.card{top:885px;width:168px;height:222px;background:var(--white);box-shadow:0 0 4px rgba(0,0,0,.15)}
.card-img{height:107px}
.card-name{position:absolute;left:13px;top:118px;font-family:"Poppins",sans-serif;font-weight:600;font-size:12px;color:var(--ink)}
.card-addr{position:absolute;left:28px;top:140px;font-size:8.5px;line-height:13px;color:var(--muted);width:135px}
.card-pin{position:absolute;left:13px;top:142px}
.card-price{position:absolute;left:18px;top:171px;font-family:"Poppins",sans-serif;font-weight:600;font-size:11px;color:var(--ink)}
.card-bar{position:absolute;left:0;bottom:0;width:100%;height:26px;background:var(--ink);display:flex;align-items:center;justify-content:space-around;color:var(--white);font-size:7.5px}
.card-bar span{display:flex;align-items:center;gap:3px}
.arrow{width:24px;height:24px}

/* locations */
.band{left:0;width:1200px;background:var(--band)}
.loc-name{left:233px;top:1300px;font-family:"Poppins",sans-serif;font-weight:700;font-size:23px;letter-spacing:7px;color:var(--ink)}
.loc-sub{left:234px;top:1332px;font-size:19px;color:var(--ink)}
.loc-text{left:234px;top:1363px;width:360px;font-size:9.3px;line-height:15px;color:var(--muted)}
.map-uk{left:660px;top:1172px;width:212px;height:406px;background:linear-gradient(180deg,#d3d3d3,#c4c4c4);border-radius:45% 40% 35% 45%/20% 25% 30% 30%}

/* testimonials */
.quote{top:1712px;width:228px}
.quote p{font-size:9.3px;line-height:15px;color:var(--muted);margin-top:12px}
.quote b{display:block;margin-top:12px;font-family:"Poppins",sans-serif;font-weight:600;font-size:8px;color:var(--ink)}

/* partners */
.partner{top:1965px;width:90px;height:70px;background:#c9c9c9;border-radius:6px}

/* map + form */
.map-area{left:0;top:2078px;width:1200px;height:228px;background:linear-gradient(90deg,#dcdcdc,#e8e8e8 50%,#dedede)}
.info-card{left:258px;top:2137px;width:187px;height:120px;background:var(--white);box-shadow:0 1px 4px rgba(0,0,0,.15);font-size:10px;color:var(--ink)}
.info-row{position:absolute;left:14px;display:flex;gap:8px;line-height:15px}
.form{left:670px;top:2140px;width:276px;height:325px;background:var(--white);box-shadow:0 1px 6px rgba(0,0,0,.15);z-index:2}
.form-title{position:absolute;left:41px;top:20px;font-family:"Poppins",sans-serif;font-weight:600;font-size:14px;color:var(--ink)}
.input{position:absolute;left:41px;width:195px;border:1px solid var(--line);font-size:8px;color:#aaa;padding:0 13px;display:flex;align-items:center}

/* footer */
.footer{left:0;top:2306px;width:1200px;height:288px;background:var(--footer);color:var(--footer-text)}
.footer .brand{color:var(--white)}
.footer .brand-square{background:var(--white)}
.f-head{font-family:"Poppins",sans-serif;font-weight:600;font-size:10px;color:var(--white)}
.f-links{font-size:9px;line-height:19px;color:var(--footer-text)}
.social{width:17px;height:17px;border-radius:50%;background:var(--white)}
</style>
</head>
<body>

<!-- Header -->
<header>
  <div class="abs brand" style="left:233px;top:37px"><span class="brand-square"></span>BRINDLE'S HOMES</div>
  <div class="abs topline">Need help or advice? Reach out to us today! <b>600-555-0182</b></div>
  <nav class="abs nav"><span>Buy</span><span>Sell</span><span>Properties</span><span>Services</span><span>About Us</span><span>Contact</span></nav>
  <div class="abs btn-outline" style="left:821px;top:45px;width:65px;height:26px">Log in</div>
  <div class="abs btn-dark" style="left:895px;top:45px;width:65px;height:26px;font-size:11px">Sign up</div>
</header>

<!-- Hero -->
<section>
  <div class="abs hero" role="img" aria-label="Photo of old wooden houses under a blue sky"></div>
  <h1 class="abs hero-title">FIND YOUR DREAM HOME JUST IN A CLICK</h1>
  <p class="abs hero-sub">Duis aute irure dolor in reprehenderit in voluptate velit esse cillum dolore eu fugiat nulla pariatur sint.</p>
  <div class="abs search"></div>
  <div class="abs field" style="left:309px;top:277px;width:136px;height:30px;justify-content:space-between;padding-right:12px">Propery Type<svg width="7" height="5" viewBox="0 0 7 5"><path d="M1 1l2.5 2.5L6 1" fill="none" stroke="#555"/></svg></div>
  <div class="abs field" style="left:455px;top:277px;width:285px;height:30px">Enter Location</div>
  <div class="abs btn-dark" style="left:749px;top:277px;width:137px;height:30px;font-family:Poppins,sans-serif;font-weight:600;font-size:8.5px">SEARCH</div>
</section>

<!-- What we do -->
<section>
  <h2 class="abs heading wwd-title">WHAT WE DO</h2>
  <p class="abs wwd-sub">Quisque porttitor nulla non erat mattis consequat.</p>
  <p class="abs wwd-text">Lorem ipsum dolor sit amet, consectetur adipiscing elit. Donec sodales tortor at nisl rutrum, at porta diam bibendum. Aenean justo mi, rutrum ut eleifend eu, ultrices eget quam. Duis cursus, felis sed fermentum ultricies, metus dui hendrerit augue, sed dignissim erat lectus nec leo. Cras sodales pharetra velit vitae fermentum. Maecenas rutrum ultrices accumsan. Vivamus sit amet sodales sem. Phasellus venenatis turpis vel odio mattis fermentum id at est. Duis ac vulputate sapien, vestibulum cursus massa. Maecenas efficitur lacus neque, at laoreet lorem congue in. Aliquam eget mauris non libero semper egestas ac a eros. Donec turpis augue, pretium vel efficitur et, cursus a odio. Quisque id elit vitae nunc convallis lobortis efficitur eget nulla. Duis hendrerit enim sed ipsum lacinia aliquam.</p>
  <div class="abs btn-dark" style="left:234px;top:730px;width:78px;height:23px;font-size:8.5px">GET IN TOUCH</div>
  <div class="abs frame" style="left:579px;top:587px;width:255px;height:179px"></div>
  <div class="abs photo" style="left:595px;top:484px;width:365px;height:263px" role="img" aria-label="Photo of a large Mediterranean style villa with gardens"></div>
</section>

<!-- Find a property -->
<section>
  <h2 class="abs heading center section-title" style="top:806px">Find A Property</h2>
  <p class="abs center section-sub" style="top:838px">Lorem ipsum dolor sit amet, consectetur adipiscing elit.</p>
  <svg class="abs arrow" style="left:194px;top:980px" viewBox="0 0 24 24"><circle cx="12" cy="12" r="11" fill="none" stroke="#333"/><path d="M17 12H7M10 9l-3 3 3 3" fill="none" stroke="#333"/></svg>
  <svg class="abs arrow" style="left:976px;top:980px" viewBox="0 0 24 24"><circle cx="12" cy="12" r="11" fill="none" stroke="#333"/><path d="M7 12h10M14 9l3 3-3 3" fill="none" stroke="#333"/></svg>

  <article class="abs card" style="left:234px">
    <div class="card-img" style="background:linear-gradient(180deg,#4a6fa5,#d9cdb8 50%,#4d6b35)" role="img" aria-label="Photo of a cottage with climbing plants"></div>
    <div class="card-name">Sweet Family Home</div>
    <svg class="card-pin" width="9" height="11" viewBox="0 0 9 11"><path d="M4.5 10.5S1 6.5 1 4.3a3.5 3.5 0 0 1 7 0C8 6.5 4.5 10.5 4.5 10.5z" fill="none" stroke="#333"/><circle cx="4.5" cy="4.3" r="1.2" fill="#333"/></svg>
    <div class="card-addr">123 Street Name, Area Name, City, Country, Zip Code</div>
    <div class="card-price">$1,200</div>
    <div class="card-bar"><span>▤ 4 Beds</span><span>⊔ 5 Baths</span><span>▥ 1200 Sqft</span></div>
  </article>
  <article class="abs card" style="left:420px">
    <div class="card-img" style="background:linear-gradient(180deg,#c9a88a,#8d8d88 50%,#5d6b45)" role="img" aria-label="Photo of a modern grey family house"></div>
    <div class="card-name">Sweet Family Home</div>
    <svg class="card-pin" width="9" height="11" viewBox="0 0 9 11"><path d="M4.5 10.5S1 6.5 1 4.3a3.5 3.5 0 0 1 7 0C8 6.5 4.5 10.5 4.5 10.5z" fill="none" stroke="#333"/><circle cx="4.5" cy="4.3" r="1.2" fill="#333"/></svg>
    <div class="card-addr">123 Street Name, Area Name, City, Country, Zip Code</div>
    <div class="card-price">$1,200</div>
    <div class="card-bar"><span>▤ 4 Beds</span><span>⊔ 5 Baths</span><span>▥ 1200 Sqft</span></div>
  </article>
  <article class="abs card" style="left:607px">
    <div class="card-img" style="background:linear-gradient(180deg,#8fb4e0,#e8e8f2 45%,#4b4b9a 70%,#bcbcbc)" role="img" aria-label="Photo of a white villa with blue roofs"></div>
    <div class="card-name">Sweet Family Home</div>
    <svg class="card-pin" width="9" height="11" viewBox="0 0 9 11"><path d="M4.5 10.5S1 6.5 1 4.3a3.5 3.5 0 0 1 7 0C8 6.5 4.5 10.5 4.5 10.5z" fill="none" stroke="#333"/><circle cx="4.5" cy="4.3" r="1.2" fill="#333"/></svg>
    <div class="card-addr">123 Street Name, Area Name, City, Country, Zip Code</div>
    <div class="card-price">$1,200</div>
    <div class="card-bar"><span>▤ 4 Beds</span><span>⊔ 5 Baths</span><span>▥ 1200 Sqft</span></div>
  </article>
  <article class="abs card" style="left:793px">
    <div class="card-img" style="background:linear-gradient(180deg,#1d2a45,#6b5a4a 45%,#2f4a6a 65%,#a0202e 85%,#2d4a22)" role="img" aria-label="Photo of a modern house with a pool at dusk"></div>
    <div class="card-name">Sweet Family Home</div>
    <svg class="card-pin" width="9" height="11" viewBox="0 0 9 11"><path d="M4.5 10.5S1 6.5 1 4.3a3.5 3.5 0 0 1 7 0C8 6.5 4.5 10.5 4.5 10.5z" fill="none" stroke="#333"/><circle cx="4.5" cy="4.3" r="1.2" fill="#333"/></svg>
    <div class="card-addr">123 Street Name, Area Name, City, Country, Zip Code</div>
    <div class="card-price">$1,200</div>
    <div class="card-bar"><span>▤ 4 Beds</span><span>⊔ 5 Baths</span><span>▥ 1200 Sqft</span></div>
  </article>
</section>

<!-- Locations -->
<section>
  <div class="abs band" style="top:1155px;height:452px"></div>
  <div class="abs loc-name">BRINDLE'S HOMES</div>
  <div class="abs loc-sub">Locations in UK</div>
  <p class="abs loc-text">Lorem ipsum dolor sit amet, consectetur adipiscing elit. Donec vehicula diam diam, non accumsan arcu tincidunt eu. Mauris lacus ante, aliquet et dui ut, pellentesque rhoncus tortor. Donec quam eros, bibendum ac justo nec, lobortis tempor eros. Nulla posuere maximus aliquam. Quisque nec eleifend quam. Suspendisse ac varius nibh, at pellentesque mi. Vivamus hendrerit eu mi vitae commodo. Phasellus ut arcu mi. Nulla sed erat sagittis, maximus ante sollicitudin, suscipit libero.</p>
  <div class="abs btn-dark" style="left:234px;top:1469px;width:125px;height:33px;font-family:Poppins,sans-serif;font-weight:600;font-size:10px">LEARN MORE</div>
  <div class="abs map-uk" role="img" aria-label="Map of the United Kingdom marking office locations"></div>
</section>

<!-- Testimonials -->
<section>
  <h2 class="abs heading center section-title" style="top:1641px">Our Client Words</h2>
  <div class="abs" style="left:580px;top:1677px;width:34px;height:1px;background:#999"></div>
  <svg class="abs arrow" style="left:194px;top:1738px" viewBox="0 0 24 24"><circle cx="12" cy="12" r="11" fill="none" stroke="#333"/><path d="M17 12H7M10 9l-3 3 3 3" fill="none" stroke="#333"/></svg>
  <svg class="abs arrow" style="left:976px;top:1738px" viewBox="0 0 24 24"><circle cx="12" cy="12" r="11" fill="none" stroke="#333"/><path d="M7 12h10M14 9l3 3-3 3" fill="none" stroke="#333"/></svg>
  <div class="abs quote" style="left:234px"><svg width="64" height="11" viewBox="0 0 64 11" fill="var(--star)"><g id="s"><polygon points="5.5,0 7,4 11,4 7.8,6.5 9,10.5 5.5,8 2,10.5 3.2,6.5 0,4 4,4"/></g><use href="#s" x="13"/><use href="#s" x="26"/><use href="#s" x="39"/><use href="#s" x="52"/></svg><p>Mauris tristique non magna vitae congue. Aenean a varius ex. Donec ultricies est sit amet sodales scelerisque. Aliquam erat volutpat.</p><b>Kelly C., UK</b></div>
  <div class="abs quote" style="left:484px"><svg width="64" height="11" viewBox="0 0 64 11" fill="var(--star)"><use href="#s"/><use href="#s" x="13"/><use href="#s" x="26"/><use href="#s" x="39"/><use href="#s" x="52"/></svg><p>Mauris tristique non magna vitae congue. Aenean a varius ex. Donec ultricies est sit amet sodales scelerisque. Aliquam erat volutpat.</p><b>Linda C., UK</b></div>
  <div class="abs quote" style="left:731px"><svg width="64" height="11" viewBox="0 0 64 11" fill="var(--star)"><use href="#s"/><use href="#s" x="13"/><use href="#s" x="26"/><use href="#s" x="39"/><use href="#s" x="52"/></svg><p>Mauris tristique non magna vitae congue. Aenean a varius ex. Donec ultricies est sit amet sodales scelerisque. Aliquam erat volutpat.</p><b>Celia L., UK</b></div>
</section>

<!-- Partners -->
<section>
  <div class="abs band" style="top:1850px;height:228px;background:#f8f8f8"></div>
  <h2 class="abs heading center section-title" style="top:1884px">Our Partners</h2>
  <p class="abs center section-sub" style="top:1917px">Lorem ipsum dolor sit amet, consectetur adipiscing elit.</p>
  <svg class="abs arrow" style="left:194px;top:1995px" viewBox="0 0 24 24"><circle cx="12" cy="12" r="11" fill="none" stroke="#333"/><path d="M17 12H7M10 9l-3 3 3 3" fill="none" stroke="#333"/></svg>
  <svg class="abs arrow" style="left:976px;top:1995px" viewBox="0 0 24 24"><circle cx="12" cy="12" r="11" fill="none" stroke="#333"/><path d="M7 12h10M14 9l3 3-3 3" fill="none" stroke="#333"/></svg>
  <div class="abs partner" style="left:278px"></div>
  <div class="abs partner" style="left:434px"></div>
  <div class="abs partner" style="left:584px"></div>
  <div class="abs partner" style="left:730px"></div>
  <div class="abs partner" style="left:858px"></div>
</section>

<!-- Contact map and form -->
<section>
  <div class="abs map-area" role="img" aria-label="Greyscale map of the office area"></div>
  <svg class="abs" style="left:462px;top:2150px" width="10" height="14" viewBox="0 0 10 14"><path d="M5 13.5S.5 8 .5 5a4.5 4.5 0 0 1 9 0C9.5 8 5 13.5 5 13.5z" fill="var(--pin)"/><circle cx="5" cy="5" r="1.6" fill="#fff"/></svg>
  <div class="abs info-card">
    <div class="info-row" style="top:14px"><svg width="10" height="13" viewBox="0 0 10 13"><path d="M5 12.5S.5 7.5.5 4.8a4.5 4.5 0 0 1 9 0C9.5 7.5 5 12.5 5 12.5z" fill="#111"/><circle cx="5" cy="4.8" r="1.6" fill="#fff"/></svg><div>BRINDLE'S HOMES<br>123 Building Name, Area Name, Street, City, Country - Zipcode</div></div>
    <div class="info-row" style="top:69px"><svg width="12" height="12" viewBox="0 0 24 24"><path d="M6.6 10.8a15 15 0 0 0 6.6 6.6l2.2-2.2c.3-.3.7-.4 1-.2 1.1.4 2.3.6 3.6.6.6 0 1 .4 1 1V20c0 .6-.4 1-1 1A17 17 0 0 1 3 4c0-.6.4-1 1-1h3.5c.6 0 1 .4 1 1 0 1.3.2 2.5.6 3.6.1.3 0 .7-.2 1z" fill="#111"/></svg><div style="font-size:11px">(600) 555-0182</div></div>
    <div class="info-row" style="top:97px"><svg width="12" height="10" viewBox="0 0 12 10"><rect width="12" height="10" fill="#111"/><path d="M1 1l5 4 5-4" fill="none" stroke="#fff"/></svg><div style="font-size:9px">info@brindlehomes-mail.example</div></div>
  </div>
  <form class="abs form">
    <div class="form-title">QUOTE TO MEETING</div>
    <div class="input" style="top:54px;height:29px;color:#111;border-color:#555">John Do |</div>
    <div class="input" style="top:89px;height:29px">Email address*</div>
    <div class="input" style="top:124px;height:29px">Phone*</div>
    <div class="input" style="top:159px;height:94px;align-items:flex-start;padding-top:12px">Enter your Question</div>
    <div class="btn-dark" style="position:absolute;left:42px;top:273px;width:91px;height:27px;font-family:Poppins,sans-serif;font-weight:600;font-size:10px">SUBMIT</div>
  </form>
</section>

<!-- Footer -->
<footer class="abs footer">
  <div class="abs brand" style="left:233px;top:88px"><span class="brand-square"></span>BRINDLE'S HOMES</div>
  <p class="abs" style="left:234px;top:116px;width:170px;font-size:9px;line-height:15px">Lorem ipsum dolor sit amet, consectetur adipiscing elit.</p>
  <div class="abs social" style="left:235px;top:158px"></div>
  <div class="abs social" style="left:257px;top:158px"></div>
  <div class="abs social" style="left:279px;top:158px"></div>
  <div class="abs social" style="left:301px;top:158px"></div>
  <div class="abs f-head" style="left:451px;top:50px">Quick link</div>
  <div class="abs f-links" style="left:451px;top:82px">Home<br>Projects<br>About</div>
  <div class="abs f-head" style="left:569px;top:50px">Help</div>
  <div class="abs f-links" style="left:569px;top:82px">Contact<br>FAQ<br>Site Map</div>
  <div class="abs" style="left:234px;top:201px;width:726px;height:1px;background:#4a4a4a"></div>
  <div class="abs" style="left:234px;top:232px;font-size:8.5px;color:#8d8d8d">Copyright © 2019 BRINDLE'S HOMES. All rights reserved.</div>
  <div class="abs" style="left:776px;top:232px;font-size:8.5px;color:#8d8d8d">Terms and conditions &nbsp;&nbsp;&nbsp;&nbsp;|&nbsp;&nbsp;&nbsp;&nbsp; Privacy policy</div>
</footer>

</body>
</html>
```